Varnel Group Limited Stationary

We are in need of business card and letterhead designs. We are looking for clean modern designs that complement the style and feel of our logo.

Industry/Entity Type

Business

```html
<!DOCTYPE html>
<html lang="en">
<head>
<meta charset="utf-8">
<title>Varnel Group Limited Stationery</title>
<link rel="stylesheet" href="https://fonts.googleapis.com/css2?family=Cormorant+Garamond:wght@500;600&display=swap">
<style>
  :root {
    --backdrop: #e4e4e7;
    --paper: #ffffff;
    --brand-blue: #2f6fbf;
    --brand-navy: #1e3c86;
    --icon-blue: #93b3da;
    --text-grey: #6a6a70;
    --rule: #b8c6dc;
  }
  html, body {
    margin: 0;
    padding: 0;
    overflow: hidden;
  }
  .canvas {
    position: relative;
    width: 1200px;
    height: 800px;
    overflow: hidden;
    background: var(--backdrop);
    font-family: "Cormorant Garamond", Georgia, serif;
  }
  .sheet {
    position: absolute;
    background: var(--paper);
    box-shadow: 0 2px 10px rgba(0,0,0,0.12);
  }

  /* Brand lockup */
  .brand {
    display: flex;
    flex-direction: column;
    align-items: center;
  }
  .brand-mark {
    border-radius: 50%;
    background: var(--brand-blue);
  }
  .brand-name {
    font-weight: 600;
    font-variant: small-caps;
    letter-spacing: 0.06em;
    color: var(--brand-navy);
    line-height: 1;
    white-space: nowrap;
  }
  .brand-rule {
    height: 1px;
    background: var(--rule);
  }

  /* Letterhead */
  .letterhead {
    left: 70px;
    top: 40px;
    width: 510px;
    height: 720px;
  }
  .letterhead .brand {
    position: absolute;
    top: 34px;
    right: 40px;
  }
  .letterhead .brand-mark { width: 20px; height: 20px; margin-bottom: 4px; }
  .letterhead .brand-name { font-size: 15px; }
  .letterhead .brand-rule { width: 96px; margin-top: 3px; }

  .social-row {
    display: flex;
    gap: 8px;
  }
  .social-dot {
    border-radius: 50%;
    background: var(--icon-blue);
    border: 2px solid #d5e1f0;
    box-sizing: border-box;
  }
  .letterhead .social-row {
    position: absolute;
    left: 36px;
    bottom: 36px;
  }
  .letterhead .social-dot { width: 28px; height: 28px; }

  .contact {
    font-weight: 500;
    color: var(--text-grey);
    text-align: right;
    line-height: 1.3;
  }
  .letterhead .contact {
    position: absolute;
    right: 40px;
    bottom: 34px;
    font-size: 12px;
  }

  /* Business card, front */
  .card-front {
    left: 650px;
    top: 70px;
    width: 400px;
    height: 230px;
  }
  .card-front .brand {
    position: absolute;
    top: 42px;
    left: 0;
    right: 0;
  }
  .card-front .brand-mark { width: 30px; height: 30px; margin-bottom: 6px; }
  .card-front .brand-name { font-size: 24px; }
  .card-front .brand-rule { width: 150px; margin-top: 4px; }
  .card-front .contact {
    position: absolute;
    left: 30px;
    bottom: 22px;
    text-align: left;
    font-size: 12px;
  }

  /* Business card, reverse */
  .card-reverse {
    left: 730px;
    top: 340px;
    width: 250px;
    height: 400px;
    overflow: hidden;
  }
  .card-reverse .brand {
    position: absolute;
    top: 58px;
    left: 0;
    right: 0;
  }
  .card-reverse .brand-mark { width: 30px; height: 30px; margin-bottom: 6px; }
  .card-reverse .brand-name { font-size: 22px; }
  .card-reverse .brand-rule { width: 140px; margin-top: 4px; }
  .pattern-field {
    position: absolute;
    left: 0;
    right: 0;
    bottom: 0;
    height: 220px;
    background: linear-gradient(180deg, #3a7bc6 0%, #2f6fbf 100%);
  }
  .card-reverse .social-row {
    position: absolute;
    left: 0;
    right: 0;
    top: 290px;
    justify-content: center;
  }
  .card-reverse .social-dot {
    width: 26px;
    height: 26px;
    background: var(--brand-blue);
    border: 2px solid #ffffff;
  }
</style>
</head>
<body>
<main class="canvas">

  <section class="sheet letterhead" aria-label="Letterhead">
    <div class="brand">
      <span class="brand-mark"></span>
      <span class="brand-name">Varnel Group</span>
      <span class="brand-rule"></span>
    </div>
    <div class="social-row" aria-label="Social links">
      <span class="social-dot"></span>
      <span class="social-dot"></span>
      <span class="social-dot"></span>
      <span class="social-dot"></span>
      <span class="social-dot"></span>
    </div>
    <address class="contact" style="font-style:normal">
      123 South Avenue West<br>
      City, Province,<br>
      Country, Zip Code<br>
      info@varnelgroup.com<br>
      www.varnelgroup.com
    </address>
  </section>

  <section class="sheet card-front" aria-label="Business card front">
    <div class="brand">
      <span class="brand-mark"></span>
      <span class="brand-name">Varnel Group</span>
      <span class="brand-rule"></span>
    </div>
    <address class="contact" style="font-style:normal">
      123 South Avenue West<br>
      City, Province, Country, Zip Code
    </address>
  </section>

  <section class="sheet card-reverse" aria-label="Business card reverse">
    <div class="brand">
      <span class="brand-mark"></span>
      <span class="brand-name">Varnel Group</span>
      <span class="brand-rule"></span>
    </div>
    <div class="pattern-field" role="img" aria-label="Blue interlocking circle pattern"></div>
    <div class="social-row" aria-label="Social links">
      <span class="social-dot"></span>
      <span class="social-dot"></span>
      <span class="social-dot"></span>
      <span class="social-dot"></span>
      <span class="social-dot"></span>
    </div>
  </section>

</main>
</body>
</html>
```